Looking for updated Letterhead and Compliments Slips to go with our new updated logo. This stationary will be used for letters to suppliers and customers so needs to be practical while also quite classic.

We are an engineering company so needs to be clean and precise

Target Market(s)

SME'S and large automotive customers

Industry/Entity Type

Automotive

Font styles to use
Sans Serif

Colors
85acd3
0356a4
0792cd
33a6d7
85abd2
ffffff

Requirements
Must have
• Address details as below
• KT Fabrications Limited
• Hallmere Road
• Brackton
• Westmereshire
• LP47 9XZ, UK
• Telephone: +44 (0)1632 960418
• Fax: +44 (0)1632 960733
• Email: sales@ktfabrications.example
• Web: www.ktfabrications.example
Nice to have
• Nice to have some element of being a British Manufacturer

```html
<!DOCTYPE html>
<html lang="en">
<head>
<meta charset="utf-8">
<title>KT Fabrications Stationery</title>
<link href="https://fonts.googleapis.com/css2?family=Open+Sans:wght@400;600&display=swap" rel="stylesheet">
<style>
  :root {
    --brand-blue: #0356a4;
    --ink: #222222;
    --rule: #1c1c1c;
    --paper: #ffffff;
    --backdrop: #d9d9d9;
  }
  * { margin: 0; padding: 0; box-sizing: border-box; }
  html, body { width: 1200px; height: 923px; overflow: hidden; }
  body {
    background: var(--backdrop);
    font-family: "Open Sans", Arial, sans-serif;
    color: var(--ink);
    position: relative;
  }
  .sheet { position: absolute; background: var(--paper); overflow: hidden; }
  .letterhead { left: 56px; top: 116px; width: 533px; height: 690px; }
  .envelope { left: 617px; top: 308px; width: 525px; height: 231px; }
  .comp-slip { left: 617px; top: 574px; width: 525px; height: 231px; }

  .brand-name {
    position: absolute;
    font-family: "Open Sans", Arial, sans-serif;
    font-weight: 600;
    font-size: 11px;
    letter-spacing: 0.3em;
    color: var(--brand-blue);
    white-space: nowrap;
  }
  .letterhead .brand-name { left: 35px; top: 88px; }
  .comp-slip .brand-name { left: 20px; top: 56px; }

  .contact-block {
    position: absolute;
    left: 386px; top: 39px;
    border-left: 1px solid #555;
    padding-left: 9px;
    font-size: 7.6px;
    line-height: 9.3px;
    font-style: normal;
    white-space: nowrap;
  }
  .company-name { color: var(--brand-blue); font-weight: 600; }
  .contact-lines { margin-top: 6px; }
  .contact-line { display: flex; align-items: center; gap: 4px; }
  .contact-line svg { width: 7px; height: 7px; fill: var(--brand-blue); flex: none; }

  .slip-address {
    position: absolute;
    left: 20px; top: 177px;
    font-size: 7px;
    line-height: 8.6px;
    font-style: normal;
    white-space: nowrap;
  }

  .footer-band {
    position: absolute; left: 0; bottom: 0; width: 100%; height: 26px;
  }
  .footer-band svg { position: absolute; inset: 0; width: 100%; height: 100%; }
  .footer-url {
    position: absolute; right: 42px; bottom: 7px;
    color: var(--paper); font-size: 10px;
  }
  .comp-slip .footer-url { right: 26px; }

  .envelope-flap { position: absolute; left: 0; top: 0; width: 525px; height: 65px; }
  .envelope .brand-name { color: var(--paper); left: 0; width: 100%; text-align: center; top: 25px; }
</style>
</head>
<body>

<section class="sheet letterhead">
  <div class="brand-name">KT FABRICATIONS</div>
  <address class="contact-block">
    <div class="company-name">KT Fabrications Limited</div>
    <div>Hallmere Road, Brackton,</div>
    <div>Westmereshire, LP47 9XZ, UK</div>
    <div class="contact-lines">
      <div class="contact-line">
        <svg viewBox="0 0 10 10"><path d="M2 0.5 L4 2.5 L3 3.6 Q4.2 5.8 6.4 7 L7.5 6 L9.5 8 L8 9.5 Q3.5 9 0.5 2 Z"/></svg>
        +44 (0)1632 960418
      </div>
      <div class="contact-line">
        <svg viewBox="0 0 10 10"><rect x="2.5" y="0.5" width="5" height="2.5"/><rect x="0.5" y="3.5" width="9" height="3.5" rx="1"/><rect x="2.5" y="7.5" width="5" height="2"/></svg>
        +44 (0)1632 960733
      </div>
      <div class="contact-line">
        <svg viewBox="0 0 10 10"><path d="M0.5 2 H9.5 V8.5 H0.5 Z"/></svg>
        sales@ktfabrications.example
      </div>
    </div>
  </address>
  <div class="footer-band">
    <svg viewBox="0 0 533 26" preserveAspectRatio="none">
      <path d="M0 4 H318 Q334 4 344 7 Q336 10 318 10 H0 Z" fill="var(--rule)"/>
      <path d="M0 26 V17 H322 C345 17 352 0 385 0 H533 V26 Z" fill="var(--brand-blue)"/>
    </svg>
    <span class="footer-url">www.ktfabrications.example</span>
  </div>
</section>

<section class="sheet envelope">
  <svg class="envelope-flap" viewBox="0 0 525 65">
    <path d="M0 0 H525 L519 45 Q516 64 494 64 H31 Q12 64 9 45 Z" fill="var(--brand-blue)"/>
  </svg>
  <div class="brand-name">KT FABRICATIONS</div>
</section>

<section class="sheet comp-slip">
  <div class="brand-name">KT FABRICATIONS</div>
  <address class="slip-address">
    <div class="company-name">KT Fabrications Limited</div>
    <div>Hallmere Road, Brackton,</div>
    <div>Westmereshire, LP47 9XZ, UK</div>
  </address>
  <div class="footer-band">
    <svg viewBox="0 0 525 26" preserveAspectRatio="none">
      <path d="M0 4 H316 Q332 4 342 7 Q334 10 316 10 H0 Z" fill="var(--rule)"/>
      <path d="M0 26 V17 H320 C342 17 350 0 382 0 H525 V26 Z" fill="var(--brand-blue)"/>
    </svg>
    <span class="footer-url">www.ktfabrications.example</span>
  </div>
</section>

</body>
</html>
```